Event Graphics for a Kid's Camp for 8 - 11 year olds

I need graphics designed for our summer camps event. These camps are for kids, 3rd - 6th grades. The design visual appeal should be geared to a 6th grade student who is 11 years old.
Primary graphic design is for a 11x17 poster.
Graphic should include the following:
-Please include cut and bleed lines.
-Main Title: SD BrightPath presents . . . Summer Camp
-Dates: Kids Camp 1 - June 23-26; Kids Camp 2 - June 26 - 29.
-Register at SDTrailweekfun.com
-Cedar Hollow Lodge Center, Deadwood, SD
-Include the name and headshot/bodyshot of our speaker: Milo Hendrick
-Include SD BrightPath logo
I will also need the images resized and redesigned for:
-a social media graphic
-Include SD BrightPath logo
-16x9 title slide
-Include SD BrightPath logo
- a postcard sized 3.5 X 5 inches
-(If possible), include name and headshot/bodyshot of speaker: Milo Hendrick
-Include SD BrightPath logo
-Event Graphic should be attractive to older kids. Open to ideas. I want rich colors but not bright fluorescent. Do not include palm trees. Our location is in a pine tree forest in the Black Hills of South Dakota. Kid-friendly designs without being childish or goofy are desired. Abstract designs, geometric shapes, designs with depth and quality could be good ideas.
My graphic design experience is limited. I will need help receiving the files I need in the various sizes. Thank you.

```html
<!DOCTYPE html>
<html lang="en">
<head>
<meta charset="utf-8">
<title>SD BrightPath Summer Camp Poster</title>
<link rel="stylesheet" href="https://fonts.googleapis.com/css2?family=Lato:wght@400;700;900&display=swap">
<style>
  :root {
    --sky: #22c0ef;
    --navy: #2b3990;
    --ink: #555a63;
    --white: #ffffff;
    --night-top: #1c2420;
    --night-mid: #2b2f28;
    --night-low: #3a3530;
    --meadow: #4f8a3a;
    --divider: #e6e8ec;
  }
  * { box-sizing: border-box; margin: 0; padding: 0; }
  html, body { width: 780px; height: 1200px; overflow: hidden; background: var(--white); }
  body { font-family: "Lato", sans-serif; position: relative; }

  .poster {
    position: absolute; left: 29px; top: 30px; width: 722px; height: 1140px;
    border: 1px solid var(--sky); overflow: hidden; background: var(--white);
  }
  .hero-backdrop {
    position: absolute; left: 0; top: 0; width: 100%; height: 820px;
    background: linear-gradient(180deg, var(--night-top) 0%, var(--night-mid) 45%, var(--night-low) 100%);
  }
  .arc { position: absolute; left: 0; top: 0; width: 722px; height: 1140px; }

  .brand {
    position: absolute; top: 150px; left: 0; width: 100%;
    display: flex; justify-content: center; align-items: center; gap: 12px;
  }
  .brand-dot { width: 22px; height: 22px; border-radius: 50%; background: var(--sky); }
  .brand-name { font-weight: 900; font-size: 46px; color: var(--sky); letter-spacing: -0.5px; }

  .presents {
    position: absolute; top: 270px; width: 100%; text-align: center;
    color: var(--white); font-weight: 900; font-size: 36px; letter-spacing: -0.3px;
  }
  .title {
    position: absolute; top: 318px; width: 100%; text-align: center;
    color: var(--sky); font-weight: 900; font-size: 83px; letter-spacing: 1px; line-height: 1.1;
  }

  .speaker-photo {
    position: absolute; left: 180px; top: 432px; width: 354px; height: 354px; border-radius: 50%;
    background: radial-gradient(circle at 50% 45%, #6d9a4a 0%, var(--meadow) 55%, #3c6e2c 100%);
    box-shadow: 0 10px 24px rgba(0,0,0,0.22);
  }
  .pointer { position: absolute; left: 190px; top: 755px; }

  .speaker-name {
    position: absolute; top: 836px; width: 100%; text-align: center;
    color: var(--navy); font-weight: 900; font-size: 40px; letter-spacing: -0.5px;
  }
  .speaker-bio {
    position: absolute; top: 897px; left: 30px; width: 662px; text-align: center;
    color: var(--ink); font-size: 12.6px; line-height: 25px;
  }

  .details { position: absolute; top: 973px; left: 0; width: 100%; height: 137px; display: flex; }
  .detail { flex: 1; padding-left: 25px; position: relative; }
  .detail + .detail { border-left: 1px solid var(--divider); }
  .pill {
    margin-top: 13px; width: 153px; height: 43px; border-radius: 22px; background: var(--sky);
    display: flex; align-items: center; gap: 14px; padding-left: 2px;
  }
  .pill-icon {
    width: 39px; height: 39px; border-radius: 50%; background: var(--navy);
    display: flex; align-items: center; justify-content: center;
  }
  .pill-label { color: var(--navy); font-weight: 900; font-size: 19px; }
  .detail-text { margin-top: 14px; color: var(--ink); font-size: 15px; line-height: 30px; }
</style>
</head>
<body>
  <main class="poster">
    <div class="hero-backdrop" role="img" aria-label="Photo of kids in sunglasses splashing in a backyard pool, darkened"></div>

    <svg class="arc" viewBox="0 0 722 1140" aria-hidden="true">
      <path d="M0,785 Q357,400 722,785 L722,1140 L0,1140 Z" fill="var(--white)"/>
      <path d="M0,785 Q357,400 722,785" fill="none" stroke="var(--sky)" stroke-width="7"/>
    </svg>

    <div class="brand">
      <span class="brand-dot"></span>
      <span class="brand-name">SD BrightPath</span>
    </div>

    <h2 class="presents">SD BrightPath Presents . . .</h2>
    <h1 class="title">SUMMER CAMP</h1>

    <div class="speaker-photo" role="img" aria-label="Portrait photo of speaker Milo Hendrick outdoors on a lawn"></div>

    <svg class="pointer" width="44" height="50" viewBox="0 0 44 50" aria-hidden="true">
      <path d="M10,4 C2,10 4,22 10,18 C14,14 8,10 6,18 C5,30 18,42 34,42" fill="none" stroke="#1d1d1d" stroke-width="2" stroke-linecap="round"/>
      <path d="M28,37 L35,42 L28,46" fill="none" stroke="#1d1d1d" stroke-width="2" stroke-linecap="round" stroke-linejoin="round"/>
    </svg>

    <h3 class="speaker-name">Milo Hendrick</h3>
    <p class="speaker-bio">At vero eos et accusamus et iusto odio dignissimos ducimus qui blanditiis praesentium voluptatum deleniti atque corrupti quos dolores et quas molestias excepturi sint occaecati cupiditate non provident, similique sunt in culpa qui officia deserunt mollitia animi, id est laborum et dolorum fuga. Et harum quidem rerum</p>

    <section class="details">
      <div class="detail">
        <div class="pill">
          <span class="pill-icon">
            <svg width="18" height="18" viewBox="0 0 18 18" aria-hidden="true">
              <rect x="1" y="3" width="16" height="14" rx="2" fill="none" stroke="var(--sky)" stroke-width="1.6"/>
              <line x1="1" y1="7" x2="17" y2="7" stroke="var(--sky)" stroke-width="1.6"/>
              <line x1="5" y1="1" x2="5" y2="4" stroke="var(--sky)" stroke-width="1.6"/>
              <line x1="13" y1="1" x2="13" y2="4" stroke="var(--sky)" stroke-width="1.6"/>
              <g fill="var(--sky)"><rect x="4" y="9" width="2" height="2"/><rect x="8" y="9" width="2" height="2"/><rect x="12" y="9" width="2" height="2"/><rect x="4" y="13" width="2" height="2"/><rect x="8" y="13" width="2" height="2"/><rect x="12" y="13" width="2" height="2"/></g>
            </svg>
          </span>
          <span class="pill-label">Dates</span>
        </div>
        <p class="detail-text">Kids Camp 1 - June 23-26<br>Kids Camp 2 - June 26 - 29</p>
      </div>
      <div class="detail">
        <div class="pill">
          <span class="pill-icon">
            <svg width="14" height="19" viewBox="0 0 14 19" aria-hidden="true">
              <path d="M7,0 C3,0 0,3 0,7 C0,12 7,19 7,19 C7,19 14,12 14,7 C14,3 11,0 7,0 Z" fill="var(--sky)"/>
              <circle cx="7" cy="7" r="2.6" fill="var(--navy)"/>
            </svg>
          </span>
          <span class="pill-label">Location</span>
        </div>
        <p class="detail-text">Cedar Hollow Lodge Center,<br>Deadwood, SD</p>
      </div>
      <div class="detail">
        <div class="pill">
          <span class="pill-icon">
            <svg width="18" height="18" viewBox="0 0 18 18" aria-hidden="true">
              <circle cx="9" cy="9" r="8" fill="var(--sky)"/>
              <path d="M5,4 C7,5 6,8 8,8 C10,9 9,11 7,12 C6,13 5,11 4,9 Z M11,3 C13,4 15,6 14,8 C12,8 11,6 11,3 Z M12,11 C14,11 14,13 12,15 C11,14 11,12 12,11 Z" fill="var(--navy)"/>
            </svg>
          </span>
          <span class="pill-label">Register</span>
        </div>
        <p class="detail-text">SDTrailweekfun.com</p>
      </div>
    </section>
  </main>
</body>
</html>
```